Sleek Design For Personal Brand Wordpress Website !!

*WORDPRESS WEBSITE*

Need a sleek and easy to navigate Wordpress website.

It will act as the hub for my personal brand.

Which means it will showcase all my social media outlets, host my most recent content like vidstream videos and podcasts...

It will also be the go to place to find all my digital products and services that I offer.

i want it to be super sleek and simple but also give a personal touch of my who I really am. You can get a good idea of who I am my checking out my Picturely (@karim.delouve)

Use these websites for ideas: www.brodyvance.example and www.nolanfitzbergen.example

Target Market(s)

Young Entrepreneurs

Industry/Entity Type

Education

Logo Text

Karim Delouve

Number of Pages Required

4 page

Font styles to use
Sans Serif

Colors
ffffff
0392cd
ec1f27

Requirements
Must have
• Social Media buttons on the home page...
• Video (also a slider) right at the top of the home page...
• Email Optin...
• Multiple pages...

```html
<!DOCTYPE html>
<html lang="en">
<head>
<meta charset="utf-8">
<title>Karim Delouve — E-Commerce Expert</title>
<link rel="stylesheet" href="https://fonts.googleapis.com/css2?family=Montserrat:wght@300;400;500;600;700&family=Quicksand:wght@400;500;600&display=swap">
<style>
  :root {
    --brand-blue: #0599cf;
    --ink: #333333;
    --ink-soft: #666666;
    --white: #ffffff;
    --paper: #ffffff;
    --mist: #efefef;
    --charcoal: #3a3a3a;
    --field: #343434;
    --field-line: #4a4a4a;
    --night: #1c1c1c;
    --chip: #333333;
  }
  * { box-sizing: border-box; margin: 0; padding: 0; }
  html, body { width: 1200px; height: 2195px; overflow: hidden; }
  body { font-family: "Montserrat", sans-serif; color: var(--ink); background: var(--paper); position: relative; }

  /* Header */
  .site-header { position: absolute; top: 0; left: 0; width: 1200px; height: 97px; background: var(--white); border-bottom: 1px solid #e4e4e4; }
  .brand { position: absolute; left: 161px; top: 30px; font-size: 29px; font-weight: 700; color: var(--brand-blue); letter-spacing: -0.3px; }
  .main-nav { position: absolute; top: 40px; left: 546px; display: flex; }
  .main-nav a { font-size: 13.5px; font-weight: 700; color: #111; text-decoration: none; margin-right: 42px; }
  .main-nav a:last-child { margin-right: 0; }

  /* Hero */
  .hero { position: absolute; top: 97px; left: 0; width: 1200px; height: 578px; overflow: hidden; }
  .hero-photo { position: absolute; inset: 0;
    background: linear-gradient(180deg, #4f6b80 0%, #3e5d70 28%, #2f4557 55%, #2a3440 100%); }
  .hero-shade { position: absolute; inset: 0; background: rgba(20, 28, 38, 0.35); }
  .hero-title { position: absolute; top: 266px; width: 100%; text-align: center; color: var(--white); font-weight: 300; font-size: 38px; letter-spacing: 0.5px; }
  .hero-lead { position: absolute; top: 332px; width: 100%; text-align: center; color: var(--white); font-size: 19px; line-height: 28px; }
  .hero-social { position: absolute; top: 416px; width: 100%; display: flex; justify-content: center; gap: 16px; color: var(--white); font-size: 13px; font-weight: 600; }
  .hero-cta { position: absolute; left: 524px; top: 475px; width: 152px; height: 47px; border: 2px solid var(--white); color: var(--white); font-size: 12px; font-weight: 700; display: flex; align-items: center; justify-content: center; letter-spacing: 0.5px; }
  .slider-arrow { position: absolute; top: 263px; width: 75px; height: 51px; background: rgba(255,255,255,0.18); display: flex; align-items: center; justify-content: center; }
  .slider-arrow.prev { left: 0; }
  .slider-arrow.next { right: 0; }

  /* About */
  .about { position: absolute; top: 675px; left: 0; width: 1200px; height: 370px; background: var(--paper); }
  .section-label { font-size: 22px; font-weight: 600; color: var(--ink); letter-spacing: 0.3px; }
  .about .section-label { position: absolute; left: 161px; top: 72px; }
  .about-text { position: absolute; left: 161px; top: 122px; width: 490px; font-size: 17.5px; line-height: 27px; color: var(--ink-soft); }
  .btn-solid { position: absolute; left: 161px; top: 245px; width: 155px; height: 47px; background: var(--brand-blue); color: var(--white); font-size: 12px; font-weight: 700; display: flex; align-items: center; justify-content: center; letter-spacing: 0.5px; }
  .portrait { position: absolute; left: 775px; top: 53px; }

  /* Recent posts */
  .recent { position: absolute; top: 1045px; left: 0; width: 1200px; height: 513px; background: var(--mist); }
  .recent .section-label { position: absolute; top: 47px; width: 100%; text-align: center; }
  .post-card { position: absolute; top: 120px; width: 263px; height: 342px; background: var(--white); box-shadow: 0 2px 6px rgba(0,0,0,0.15); }
  .post-card:nth-of-type(1) { left: 161px; }
  .post-card:nth-of-type(2) { left: 468px; }
  .post-card:nth-of-type(3) { left: 776px; }
  .post-thumb { height: 155px; position: relative; display: flex; align-items: center; justify-content: center; }
  .thumb-meeting { background: linear-gradient(160deg, #a89a8a, #6d7b8c 60%, #4f5d6f); }
  .thumb-cafe { background: linear-gradient(160deg, #c9b9a4, #8b7866 55%, #5a4c42); }
  .thumb-beach { background: linear-gradient(180deg, #6b9bbd, #3f6f8f 50%, #2b3a4a); }
  .post-date { position: absolute; left: 24px; top: 189px; font-size: 11px; font-weight: 600; color: var(--brand-blue); display: flex; align-items: center; gap: 4px; }
  .post-title { position: absolute; left: 25px; top: 206px; width: 230px; font-family: "Quicksand", sans-serif; font-size: 19px; font-weight: 500; line-height: 27px; color: var(--ink); }
  .post-more { position: absolute; left: 26px; top: 278px; width: 97px; height: 29px; background: var(--chip); color: var(--white); font-size: 8px; font-weight: 700; display: flex; align-items: center; justify-content: center; }

  /* Contact */
  .contact { position: absolute; top: 1558px; left: 0; width: 1200px; height: 418px; background: var(--charcoal); }
  .contact .section-label { position: absolute; top: 49px; width: 100%; text-align: center; color: var(--white); }
  .field { position: absolute; background: var(--field); border: 1px solid var(--field-line); border-radius: 4px; color: var(--white); font-size: 13.5px; padding-left: 19px; display: flex; align-items: center; }
  .field.name { left: 266px; top: 123px; width: 299px; height: 47px; border: 2px solid #e8e8e8; background: #2e2e2e; color: #8a8a8a; }
  .field.address { left: 635px; top: 123px; width: 299px; height: 47px; }
  .field.message { left: 266px; top: 198px; width: 668px; height: 92px; align-items: flex-start; padding-top: 16px; }
  .send { position: absolute; left: 266px; top: 318px; width: 668px; height: 47px; background: var(--brand-blue); border-radius: 4px; color: var(--white); font-size: 13.5px; display: flex; align-items: center; justify-content: center; }

  /* Footer */
  .site-footer { position: absolute; top: 1976px; left: 0; width: 1200px; height: 219px; background: var(--night); color: var(--white); text-align: center; }
  .footer-contacts { position: absolute; top: 48px; width: 100%; font-size: 14.5px; font-weight: 700; display: flex; justify-content: center; gap: 30px; }
  .footer-brand { position: absolute; top: 94px; width: 100%; font-size: 24px; font-weight: 700; }
  .footer-social { position: absolute; top: 148px; width: 100%; display: flex; justify-content: center; gap: 16px; font-size: 13px; font-weight: 600; }
</style>
</head>
<body>

<header class="site-header">
  <div class="brand">KARIM DELOUVE</div>
  <nav class="main-nav">
    <a href="#">HOME</a>
    <a href="#">ABOUT ME</a>
    <a href="#">BLOG</a>
    <a href="#">TRAINING</a>
    <a href="#">CONTACT ME</a>
  </nav>
</header>

<section class="hero">
  <div class="hero-photo" role="img" aria-label="Photo of Karim smiling in sunglasses, holding a phone on a seaside terrace"></div>
  <div class="hero-shade"></div>
  <a class="slider-arrow prev" aria-label="Previous slide">
    <svg width="14" height="22" viewBox="0 0 14 22"><path d="M12 2 L3 11 L12 20" fill="none" stroke="#fff" stroke-width="2"/></svg>
  </a>
  <a class="slider-arrow next" aria-label="Next slide">
    <svg width="14" height="22" viewBox="0 0 14 22"><path d="M2 2 L11 11 L2 20" fill="none" stroke="#fff" stroke-width="2"/></svg>
  </a>
  <h1 class="hero-title">E-COMMERCE EXPERT</h1>
  <p class="hero-lead">Inspiring &amp; Helping Entrepreneurs around<br>the world achieve success....</p>
  <div class="hero-social"><span>Friendspace</span><span>Chirper</span><span>Picturely</span></div>
  <a class="hero-cta">LEARN MORE</a>
</section>

<section class="about">
  <h2 class="section-label">ABOUT ME</h2>
  <p class="about-text">Lorem ipsum dolor sit amet, consectetur adipisicing elit, sed do eiusmod tempor incididunt ut labore et dolore magna aliqua. Ut enim ad minim.</p>
  <a class="btn-solid">LEARN MORE</a>
  <svg class="portrait" width="264" height="264" viewBox="0 0 264 264">
    <circle cx="132" cy="132" r="130" fill="#fff" stroke="var(--brand-blue)" stroke-width="3.5"/>
    <circle cx="132" cy="132" r="113" fill="#d9d9d9" role="img" aria-label="Portrait of Karim in glasses and a black tee"/>
  </svg>
</section>

<section class="recent">
  <h2 class="section-label">RECENT POST</h2>

  <article class="post-card">
    <div class="post-thumb thumb-meeting" role="img" aria-label="Team meeting around a conference table"></div>
    <div class="post-date"><svg width="9" height="9" viewBox="0 0 10 10"><circle cx="5" cy="5" r="4" fill="none" stroke="currentColor" stroke-width="1.2"/><path d="M5 2.6V5h2" fill="none" stroke="currentColor" stroke-width="1.1"/></svg>25 December, 2017</div>
    <h3 class="post-title">Best Way to Overcome Frustration In Sales</h3>
    <a class="post-more">SEE MORE</a>
  </article>

  <article class="post-card">
    <div class="post-thumb thumb-cafe" role="img" aria-label="Young man with a phone in a busy café"></div>
    <div class="post-date"><svg width="9" height="9" viewBox="0 0 10 10"><circle cx="5" cy="5" r="4" fill="none" stroke="currentColor" stroke-width="1.2"/><path d="M5 2.6V5h2" fill="none" stroke="currentColor" stroke-width="1.1"/></svg>25 December, 2017</div>
    <h3 class="post-title">How to Increase Your Income While Moving..</h3>
    <a class="post-more">SEE MORE</a>
  </article>

  <article class="post-card">
    <div class="post-thumb thumb-beach" role="img" aria-label="Video still of Karim by the sea">
      <svg width="60" height="60" viewBox="0 0 60 60"><circle cx="30" cy="30" r="27" fill="rgba(0,0,0,0.25)" stroke="#fff" stroke-width="4"/><path d="M24 18 L42 30 L24 42 Z" fill="#fff"/></svg>
    </div>
    <div class="post-date"><svg width="9" height="9" viewBox="0 0 10 10"><circle cx="5" cy="5" r="4" fill="none" stroke="currentColor" stroke-width="1.2"/><path d="M5 2.6V5h2" fill="none" stroke="currentColor" stroke-width="1.1"/></svg>25 December, 2017</div>
    <h3 class="post-title">How I've made Over 6 Figures In Door-To...</h3>
    <a class="post-more">SEE MORE</a>
  </article>
</section>

<section class="contact">
  <h2 class="section-label">GET IN TOUCH WITH ME</h2>
  <div class="field name">Enter your name</div>
  <div class="field address">Enter your adresse</div>
  <div class="field message">Enter your message</div>
  <a class="send">Send Message</a>
</section>

<footer class="site-footer">
  <div class="footer-contacts"><span>+01 55 010 2468</span><span>OR</span><span>HELLO@DELOUVESTUDIO.EXAMPLE</span></div>
  <div class="footer-brand">KARIM DELOUVE</div>
  <div class="footer-social"><span>Friendspace</span><span>Chirper</span><span>Picturely</span></div>
</footer>

</body>
</html>
```